Dental Office Business Card

We need a business card for our pediatric dentistry office.
On one side the design needs to contain the following:
our logo (attached)
Corvin Kids Dental
Tamsin Vetrakovich, DDS
Board Certified Pediatric Dentist
Tel: (617) 555-0148)
Fax: (617) 555-0193
Email: info@corvinkidsdental.example
Web: www.corvinkidsdental.example
Address: 42 Brambury Ln, Suite 208, Hollisford, MA 01799

On the other side of the card, the design needs to have an appointment reminder (date and time as well as day of the week) similar to the design attached (no need for appointment reason “For”)

```html
<!DOCTYPE html>
<html lang="en">
<head>
<meta charset="utf-8">
<title>Corvin Kids Dental – Business Card</title>
<link rel="stylesheet" href="https://fonts.googleapis.com/css2?family=Source+Sans+3:wght@400;600;700&display=swap">
<style>
  :root {
    --ink: #231f20;
    --mint: #a8dcad;
    --card: #ffffff;
    --backdrop: #2b2b2b;
    --rule: #8a8a8a;
  }
  * { margin: 0; padding: 0; box-sizing: border-box; }
  html, body { width: 1093px; height: 1200px; overflow: hidden; }
  body {
    position: relative;
    background: var(--backdrop);
    font-family: "Source Sans 3", "Myriad Pro", sans-serif;
    color: var(--ink);
  }
  .card {
    position: absolute;
    left: 265px;
    width: 578px;
    height: 356px;
    background: var(--card);
    border-radius: 22px;
    overflow: hidden;
  }
  .card--front { top: 226px; }
  .card--back { top: 621px; }
  .card__band {
    position: absolute; left: 0; right: 0; bottom: 0;
    height: 12px; background: var(--mint);
  }

  /* Front */
  .identity { position: absolute; left: 26px; top: 55px; }
  .identity__name { font-size: 22px; font-weight: 700; line-height: 1; }
  .identity__name span { font-weight: 400; }
  .identity__title { font-size: 16.5px; margin-top: 4px; }

  .brand {
    position: absolute; right: 22px; top: 30px;
    display: flex; align-items: center; gap: 12px;
  }
  .brand__dot { width: 48px; height: 48px; border-radius: 50%; background: var(--mint); flex: none; }
  .brand__name {
    font-weight: 700; text-align: right; line-height: 1;
  }
  .brand__name .word { display: block; font-size: 50px; }
  .brand__name .tag { display: block; font-size: 22px; letter-spacing: 0.5px; margin-top: 4px; }

  .contacts { position: absolute; left: 27px; top: 242px; list-style: none; }
  .contacts li {
    display: flex; align-items: center; gap: 7px;
    font-size: 16.5px; line-height: 20.7px;
  }
  .contacts svg { width: 15px; height: 15px; fill: var(--mint); flex: none; }

  .address {
    position: absolute; right: 22px; top: 283px;
    font-size: 16.5px; line-height: 20.7px; text-align: right; font-style: normal;
  }

  /* Back */
  .reminder__mark {
    position: absolute; left: 38px; top: 30px;
    width: 100px; height: 100px; border-radius: 50%; background: var(--mint);
  }
  .reminder__heading {
    position: absolute; left: 163px; top: 45px; width: 256px;
    text-align: center; font-weight: 700; line-height: 1;
  }
  .reminder__heading .line1 { display: block; font-size: 37px; letter-spacing: 2px; }
  .reminder__heading .line2 { display: block; font-size: 36px; margin-top: 2px; }

  .field {
    position: absolute; left: 92px; width: 398px;
    display: flex; align-items: flex-end; font-size: 16.5px;
  }
  .field__label { width: 52px; flex: none; }
  .field__line { flex: 1; border-bottom: 1px solid var(--rule); height: 1px; margin-bottom: 5px; position: relative; }
  .field--date { top: 169px; }
  .field--time { top: 285px; }
  .field__suffix { position: absolute; right: 0; bottom: 2px; font-size: 16.5px; }

  .weekdays {
    position: absolute; left: 92px; top: 222px; width: 398px;
    display: flex; justify-content: space-between; list-style: none; font-size: 17.5px;
  }
  .weekdays li { display: flex; align-items: center; gap: 4px; }
  .weekdays .box { width: 12px; height: 12px; border: 1px solid var(--ink); }
</style>
</head>
<body>

<section class="card card--front" aria-label="Business card front">
  <div class="identity">
    <p class="identity__name">Tamsin Vetrakovich<span>, DDS</span></p>
    <p class="identity__title">Board Certified Pediatric Dentist</p>
  </div>

  <div class="brand">
    <div class="brand__dot"></div>
    <p class="brand__name"><span class="word">Corvin</span><span class="tag">KIDS DENTAL</span></p>
  </div>

  <ul class="contacts">
    <li>
      <svg viewBox="0 0 24 24" aria-hidden="true"><path d="M6.6 10.8a15 15 0 0 0 6.6 6.6l2.2-2.2a1 1 0 0 1 1-.25 11.4 11.4 0 0 0 3.6.57 1 1 0 0 1 1 1V20a1 1 0 0 1-1 1A17 17 0 0 1 3 4a1 1 0 0 1 1-1h3.5a1 1 0 0 1 1 1c0 1.250.2 2.450.57 3.57a1 1 0 0 1-.25 1z"/></svg>
      (617) 555-0148)
    </li>
    <li>
      <svg viewBox="0 0 24 24" aria-hidden="true"><path d="M6 2h12v5H6zM3 8h18a2 2 0 0 1 2 2v7h-4v5H5v-5H1v-7a2 2 0 0 1 2-2zm4 8v4h10v-4z"/></svg>
      (617) 555-0193
    </li>
    <li>
      <svg viewBox="0 0 24 24" aria-hidden="true"><path d="M2 5h20v14H2zm2 2v.5l8 5.5 8-5.5V7l-8 5.2z"/></svg>
      info@corvinkidsdental.example
    </li>
    <li>
      <svg viewBox="0 0 24 24" aria-hidden="true"><circle cx="12" cy="12" r="9" fill="none" stroke="#a8dcad" stroke-width="2"/><path d="M3 12h18M12 3c3 3 3 15 0 18M12 3c-3 3-3 15 0 18" fill="none" stroke="#a8dcad" stroke-width="1.6"/></svg>
      www.corvinkidsdental.example
    </li>
  </ul>

  <address class="address">
    42 Brambury Ln, Suite 208<br>
    Hollisford, MA 01799
  </address>

  <div class="card__band"></div>
</section>

<section class="card card--back" aria-label="Appointment reminder card back">
  <div class="reminder__mark"></div>
  <h1 class="reminder__heading">
    <span class="line1">APPOINTMENT</span>
    <span class="line2">Reminder</span>
  </h1>

  <div class="field field--date">
    <span class="field__label">DATE:</span>
    <span class="field__line"></span>
  </div>

  <ul class="weekdays">
    <li><span class="box"></span>Mon</li>
    <li><span class="box"></span>Tue</li>
    <li><span class="box"></span>Wed</li>
    <li><span class="box"></span>Thu</li>
    <li><span class="box"></span>Fri</li>
    <li><span class="box"></span>Sat</li>
    <li><span class="box"></span>Sun</li>
  </ul>

  <div class="field field--time">
    <span class="field__label">TIME:</span>
    <span class="field__line"><span class="field__suffix">AM/PM</span></span>
  </div>

  <div class="card__band"></div>
</section>

</body>
</html>
```